nonprofit organization looking for sleek new design

We need a fresh new look for this nonprofit organization, Tidewater Allies for Learning and Mutual Aid, INC (TALMA, Inc.). This organization provides educational, nutritional, dental health, and specialized services to Cedar Step children, aiming to support families meeting federal income poverty guidelines. Our mission is clear: "Creating a brighter future for the children and la familia." We focus on child development, family wellness, staff growth, and community partnerships.

```html
<!DOCTYPE html>
<html lang="en">
<head>
<meta charset="utf-8">
<title>TALMA, Inc. | Transforming Lives in Your Community</title>
<link href="https://fonts.googleapis.com/css2?family=Archivo:wght@500;600;700;800;900&family=Arimo:wght@400;700&display=swap" rel="stylesheet">
<style>
:root{
  --blue:#2b46a8;
  --blue-deep:#22398f;
  --red:#e3242b;
  --ink:#1b1b1f;
  --text:#3c3c44;
  --page:#f2f0f3;
  --maroon:#7b2a5f;
  --white:#ffffff;
}
*{box-sizing:border-box;margin:0;padding:0}
html,body{width:1200px;height:4724px;overflow:hidden;background:var(--page)}
body{font-family:"Arimo",Arial,sans-serif;color:var(--text)}
.canvas{position:relative;width:1200px;height:4724px;overflow:hidden;
  background:
    radial-gradient(ellipse 520px 700px at 1000px 1500px,rgba(210,190,235,.55),transparent 70%),
    radial-gradient(ellipse 600px 500px at 400px 1700px,rgba(180,195,245,.45),transparent 70%),
    radial-gradient(ellipse 700px 600px at 900px 4000px,rgba(215,195,235,.5),transparent 70%),
    var(--page)}
.abs{position:absolute}
.display{font-family:"Archivo",Arial,sans-serif;font-weight:800;color:var(--ink);text-transform:uppercase;letter-spacing:.5px}

/* top bar */
.topbar{left:0;top:0;width:1200px;height:31px;background:var(--blue);color:#fff;font-size:13px}
.topbar .contact{position:absolute;top:8px;display:flex;align-items:center;gap:6px}
.donate{position:absolute;left:945px;top:0;width:156px;height:31px;background:var(--red);color:#fff;font-family:"Archivo",sans-serif;font-weight:700;font-size:13px;display:flex;align-items:center;justify-content:center;gap:5px}
/* nav */
.navbar{left:0;top:31px;width:1200px;height:66px;background:#fff}
.brand{position:absolute;left:101px;top:14px;display:flex;align-items:center;gap:8px}
.brand-dot{width:38px;height:38px;border-radius:50%;background:var(--blue)}
.brand-name{font-family:"Archivo",sans-serif;font-weight:700;font-size:11.5px;line-height:14px;color:var(--blue);text-transform:uppercase}
.nav-links{position:absolute;top:25px;font-size:14px;color:var(--ink)}
.nav-links span{position:absolute;white-space:nowrap}
.nav-links .active{color:var(--red)}

/* hero */
.hero{left:0;top:97px;width:1200px;height:740px}
.hero-title{left:0;width:1200px;top:310px;text-align:center;color:#fff;font-size:50px;line-height:56px;font-weight:800;text-shadow:0 2px 8px rgba(0,0,0,.35)}
.hero-sub{left:0;width:1200px;top:432px;text-align:center;color:#fff;font-size:16px;letter-spacing:.3px;text-shadow:0 1px 4px rgba(0,0,0,.4)}
.btn{display:flex;align-items:center;justify-content:center;background:var(--red);color:#fff;font-family:"Archivo",sans-serif;font-weight:700;font-size:14px;text-transform:uppercase}
.hero-btn{left:517px;top:473px;width:166px;height:38px}
.explore{left:0;width:1200px;top:654px;text-align:center;color:#fff;font-family:"Archivo",sans-serif;font-weight:600;font-size:16px}

.ghost-num{font-family:"Archivo",sans-serif;font-weight:900;font-size:150px;line-height:1;
  background:linear-gradient(180deg,#d9d6de 0%,rgba(242,240,243,0) 90%);-webkit-background-clip:text;background-clip:text;color:transparent}

/* services */
.sec-title{font-size:62px;line-height:58px}
.body-copy{font-size:15px;line-height:32px;text-align:justify}
.arrow-btn{width:44px;height:44px;display:flex;align-items:center;justify-content:center;border-radius:3px}
.arrow-prev{left:100px;top:1253px;border:1px solid #bdbac2;background:#eeecef}
.arrow-next{left:152px;top:1253px;background:#2b2b30}
.cards-band{left:563px;top:974px;width:637px;height:191px;background:linear-gradient(160deg,var(--blue) 30%,#6f3a8e 70%,var(--red));border-radius:14px 0 0 14px}
.card{position:absolute;top:1020px;width:241px;height:279px;background:#fff;border-radius:6px;box-shadow:0 4px 14px rgba(0,0,0,.12);padding:6px}
.card-photo{width:229px;height:219px;border-radius:4px}
.card-label{position:absolute;left:14px;bottom:18px;font-family:"Archivo",sans-serif;font-weight:700;font-size:18px;color:var(--ink)}
.card-go{position:absolute;right:14px;bottom:14px;width:28px;height:28px;border-radius:50%;background:var(--blue);display:flex;align-items:center;justify-content:center}

/* opportunities */
.opp-frame{left:123px;top:1479px;width:437px;height:450px;background:#fff;padding:10px;box-shadow:0 6px 20px rgba(0,0,0,.12)}
.opp-photo{width:100%;height:100%}
.sq{width:112px;height:103px;display:flex;align-items:center;justify-content:center}
.select{left:655px;top:1908px;width:443px;height:44px;background:#fff;border:1px solid #dcd9e0;border-radius:4px;font-size:12.5px;color:#333;padding:0 18px;display:flex;align-items:center;justify-content:space-between}

/* soar */
.soar{left:0;top:2090px;width:1200px;height:719px;background:
  radial-gradient(ellipse 500px 300px at 200px 200px,rgba(255,255,255,.06),transparent 70%),
  radial-gradient(ellipse 500px 400px at 1000px 600px,rgba(0,0,0,.08),transparent 70%),var(--blue)}
.soar .ghost-num{background:linear-gradient(180deg,rgba(255,255,255,.18),rgba(255,255,255,0) 90%);-webkit-background-clip:text;background-clip:text}
.soar-title{left:0;width:1200px;top:90px;text-align:center;color:#fff;font-size:64px;line-height:60px}
.soar-copy{left:0;width:1200px;top:238px;text-align:center;color:#fff;font-size:15px;line-height:31px}
.stat{position:absolute;top:344px;width:340px;text-align:center;color:#fff}
.stat-num{margin:0 auto;width:158px;height:158px;border-radius:50%;background:var(--maroon);display:flex;align-items:center;justify-content:center;font-family:"Archivo",sans-serif;font-weight:700;font-size:60px}
.stat-label{margin-top:14px;font-family:"Archivo",sans-serif;font-weight:700;font-size:20px}
.stat-copy{margin-top:16px;font-size:15px;line-height:31px}

/* testimonial */
.quote-bg{left:0;top:2809px;width:1200px;height:620px}
.quote-box{left:193px;top:2908px;width:816px;height:422px;background:linear-gradient(180deg,rgba(185,198,240,.92),rgba(167,210,227,.92));clip-path:polygon(1% 2%,20% 0,45% 1.5%,70% 0,99% 1.5%,100% 30%,99% 60%,100% 98%,70% 100%,40% 98.5%,15% 100%,0 98%,1% 60%,0 30%)}
.quote-head{left:193px;width:816px;top:3010px;text-align:center;font-family:"Archivo",sans-serif;font-weight:700;font-size:16px;line-height:31px;color:var(--ink)}
.quote-copy{left:193px;width:816px;top:3084px;text-align:center;font-size:15px;line-height:32px;color:#333}
.quote-name{left:193px;width:816px;top:3206px;text-align:center;font-family:"Archivo",sans-serif;font-weight:700;font-size:16px;color:var(--ink)}
.dots{left:0;width:1200px;top:3278px;display:flex;justify-content:center;gap:14px}
.dots i{width:12px;height:12px;border-radius:50%;background:#fff;display:block}

/* initiatives */
.init-title{left:0;width:1170px;top:3460px;text-align:center;font-size:52px;line-height:52px}
.init-copy{left:0;width:1184px;top:3568px;text-align:center;font-size:15px;line-height:32px}
.init{position:absolute;top:3674px;width:305px;text-align:center}
.init-photo{width:305px;height:297px;border-radius:70px 70px 60px 60px / 60px 60px 70px 70px}
.init h3{margin-top:24px;font-family:"Archivo",sans-serif;font-weight:800;font-size:26px;color:var(--ink)}
.init p{margin-top:12px;font-size:15px;line-height:32px}
.init .btn{margin:16px auto 0;width:166px;height:39px}

/* footer */
.footer{left:0;top:4268px;width:1200px;height:456px;background:var(--blue);color:#fff}
.foot-brand{position:absolute;left:104px;top:84px;display:flex;align-items:center;gap:8px}
.foot-brand .brand-dot{background:#fff}
.foot-brand .brand-name{color:#fff}
.socials{position:absolute;left:165px;top:142px;display:flex;gap:17px}
.socials i{display:block;width:36px;height:36px;border-radius:50%;background:#fff}
.foot-col{position:absolute;top:72px}
.foot-col h4{font-family:"Archivo",sans-serif;font-weight:700;font-size:18px;margin-bottom:14px}
.foot-col li{list-style:none;font-size:15px;line-height:36.4px}
.foot-col li::before{content:"»";margin-right:8px}
.contact-row{display:flex;gap:12px;font-size:15px;line-height:24px;margin-bottom:22px}
.ic{flex:none;width:30px;height:30px;border-radius:50%;border:1px solid rgba(255,255,255,.6);display:flex;align-items:center;justify-content:center}
.foot-rule{position:absolute;left:101px;top:387px;width:998px;height:1px;background:rgba(255,255,255,.3)}
.copyright{position:absolute;left:0;width:1200px;top:412px;text-align:center;font-size:14px}
</style>
</head>
<body>
<div class="canvas">

  <!-- top bar -->
  <div class="abs topbar">
    <div class="contact" style="left:650px">
      <svg width="13" height="13" viewBox="0 0 24 24"><path fill="#fff" d="M6.6 10.8a15 15 0 0 0 6.6 6.6l2.2-2.2c.3-.3.7-.4 1-.2 1.1.4 2.3.6 3.6.6.6 0 1 .4 1 1V20c0 .6-.4 1-1 1A17 17 0 0 1 3 4c0-.6.4-1 1-1h3.5c.6 0 1 .4 1 1 0 1.3.2 2.5.6 3.6.1.3 0 .7-.2 1z"/></svg>
      757.555.0148
    </div>
    <div class="contact" style="left:780px">
      <svg width="15" height="12" viewBox="0 0 24 18"><rect x="1" y="1" width="22" height="16" fill="none" stroke="#fff" stroke-width="2"/><path d="M1 1l11 9 11-9" fill="none" stroke="#fff" stroke-width="2"/></svg>
      hello@talmaallies.org
    </div>
    <div class="donate">
      <svg width="12" height="11" viewBox="0 0 24 22"><path fill="#fff" d="M12 21.4 10.6 20C5.4 15.4 2 12.3 2 8.5 2 5.4 4.4 3 7.5 3c1.7 0 3.4.8 4.5 2.1C13.1 3.8 14.8 3 16.5 3 19.6 3 22 5.4 22 8.5c0 3.8-3.4 6.9-8.6 11.5z"/></svg>
      DONATE NOW
    </div>
  </div>

  <!-- nav -->
  <nav class="abs navbar">
    <div class="brand">
      <span class="brand-dot"></span>
      <span class="brand-name">Tidewater Allies for Learning<br>and Mutual Aid, INC</span>
    </div>
    <div class="nav-links">
      <span class="active" style="left:417px">Home</span>
      <span style="left:485px">Services</span>
      <span style="left:571px">Administration</span>
      <span style="left:695px">School Readiness</span>
      <span style="left:846px">Employment</span>
      <span style="left:958px">About Us</span>
      <span style="left:1048px">Contact</span>
    </div>
  </nav>

  <!-- hero -->
  <section class="abs hero">
    <svg width="1200" height="740" viewBox="0 0 1200 740" style="position:absolute;left:0;top:0">
      <defs>
        <linearGradient id="heroFill" x1="0" y1="0" x2="0" y2="1">
          <stop offset="0" stop-color="#4f86cc"/>
          <stop offset=".28" stop-color="#9fbbd6"/>
          <stop offset=".45" stop-color="#3f5e3a"/>
          <stop offset=".7" stop-color="#7d7a3a"/>
          <stop offset="1" stop-color="#b0914f"/>
        </linearGradient>
        <radialGradient id="heroCanopy" cx=".45" cy=".2" r=".5">
          <stop offset="0" stop-color="#f2c318" stop-opacity=".75"/>
          <stop offset=".45" stop-color="#e2452c" stop-opacity=".45"/>
          <stop offset=".8" stop-color="#2b56c4" stop-opacity=".25"/>
          <stop offset="1" stop-color="#2b56c4" stop-opacity="0"/>
        </radialGradient>
        <radialGradient id="heroShade" cx=".5" cy=".55" r=".5">
          <stop offset="0" stop-color="#000" stop-opacity=".28"/>
          <stop offset="1" stop-color="#000" stop-opacity="0"/>
        </radialGradient>
      </defs>
      <path d="M0 620 Q600 820 1200 620 V650 Q600 850 0 650 Z" fill="var(--blue)"/>
      <g role="img" aria-label="Children outdoors lifting a rainbow parachute on a grassy hill">
        <path d="M0 0 H1200 V620 Q600 790 0 620 Z" fill="url(#heroFill)"/>
        <path d="M0 0 H1200 V620 Q600 790 0 620 Z" fill="url(#heroCanopy)"/>
        <path d="M0 0 H1200 V620 Q600 790 0 620 Z" fill="url(#heroShade)"/>
      </g>
    </svg>
    <h1 class="abs display hero-title" style="color:#fff">Transforming Lives<br>In Your Community</h1>
    <p class="abs hero-sub">LEADING THE WAY FOR CHANGE, PROGRESS, AND GROWTH.</p>
    <a class="abs btn hero-btn">Take Action »</a>
    <span class="abs explore">EXPLORE</span>
  </section>

  <!-- services -->
  <span class="abs ghost-num" style="left:330px;top:915px">01</span>
  <h2 class="abs display sec-title" style="left:100px;top:955px">TALMA<br>Services</h2>
  <p class="abs body-copy" style="left:100px;top:1088px;width:406px">TALMA, Inc. is always interested in taking applications for pregnant women, children and children with Disabilities Ages 0-4 Years old. The program ensures your child is ready for school by providing</p>
  <div class="abs arrow-btn arrow-prev">
    <svg width="26" height="12" viewBox="0 0 26 12"><path d="M25 6H2M7 1 2 6l5 5" fill="none" stroke="#888" stroke-width="1.5"/></svg>
  </div>
  <div class="abs arrow-btn arrow-next">
    <svg width="26" height="12" viewBox="0 0 26 12"><path d="M1 6h23M19 1l5 5-5 5" fill="none" stroke="#fff" stroke-width="1.5"/></svg>
  </div>

  <div class="abs cards-band"></div>
  <div class="card" style="left:611px">
    <div class="card-photo" role="img" aria-label="Two children looking at a tablet together" style="background:radial-gradient(ellipse at 40% 45%,#a5795a,transparent 60%),linear-gradient(160deg,#8d6a52,#4a362c 60%,#36457a)"></div>
    <span class="card-label">EDUCATIONAL</span>
    <span class="card-go"><svg width="14" height="12" viewBox="0 0 14 12"><path d="M1 6h11M7 1l5 5-5 5" fill="none" stroke="#fff" stroke-width="1.8"/></svg></span>
  </div>
  <div class="card" style="left:873px">
    <div class="card-photo" role="img" aria-label="Children preparing fresh vegetables in a kitchen" style="background:radial-gradient(ellipse at 60% 40%,#3f6fc2,transparent 55%),linear-gradient(180deg,#d6d8dc,#b9c2cf 40%,#6e9a3a 75%,#c8402e)"></div>
    <span class="card-label">NUTRITIONAL</span>
    <span class="card-go"><svg width="14" height="12" viewBox="0 0 14 12"><path d="M1 6h11M7 1l5 5-5 5" fill="none" stroke="#fff" stroke-width="1.8"/></svg></span>
  </div>
  <div class="card" style="left:1137px">
    <div class="card-photo" role="img" aria-label="Smiling child at a dental visit" style="background:linear-gradient(160deg,#f0dfcc,#d9b693)"></div>
    <span class="card-label">DENTAL</span>
  </div>

  <!-- opportunities -->
  <div class="abs sq" style="left:101px;top:1457px;background:var(--blue);z-index:2">
    <svg width="40" height="20" viewBox="0 0 40 20"><path d="M39 10H3M11 2 3 10l8 8" fill="none" stroke="#fff" stroke-width="2"/></svg>
  </div>
  <div class="abs opp-frame">
    <div class="opp-photo" role="img" aria-label="Group of women holding certificates at a graduation ceremony" style="background:radial-gradient(ellipse 60% 20% at 50% 62%,rgba(240,236,230,.55),transparent 70%),linear-gradient(180deg,#dcdbe0 0%,#2c2c33 14%,#2c2c33 24%,#c9c6cc 32%,#6e5a55 50%,#2a2a33 72%,#2f3f82 100%)"></div>
  </div>
  <div class="abs sq" style="left:484px;top:1901px;background:var(--red)">
    <svg width="40" height="20" viewBox="0 0 40 20"><path d="M1 10h36M29 2l8 8-8 8" fill="none" stroke="#fff" stroke-width="2"/></svg>
  </div>
  <span class="abs ghost-num" style="left:932px;top:1475px">02</span>
  <h2 class="abs display" style="left:651px;top:1556px;font-size:47px;line-height:50px">Opportunityes<br>That Help Our<br>Community Grow</h2>
  <p class="abs body-copy" style="left:655px;top:1724px;width:443px">Sed ut perspiciatis unde omnis iste natus error sit voluptatem accusantium doloremque laudantium, totam rem aperiam, eaque ipsa quae ab illo inventore veritatis et quasi architecto beatae vitae dicta sunt explicabo. Nemo enim ipsam voluptatem quia voluptas sit aspernatur aut odit aut fugit</p>
  <div class="abs select">
    <span>I want to search...education opportunities</span>
    <svg width="16" height="9" viewBox="0 0 16 9"><path d="M1 1l7 7 7-7" fill="none" stroke="#333" stroke-width="1.5"/></svg>
  </div>

  <!-- community soar -->
  <section class="abs soar">
    <span class="abs ghost-num" style="left:789px;top:55px">03</span>
    <h2 class="abs display soar-title" style="color:#fff">Together Our<br>#CommunitiesSoar</h2>
    <p class="abs soar-copy">Sed ut perspiciatis unde omnis iste natus r sit voluptatem accusantium doloremque laudantium, totam rem aperiam,<br>eaque ipsa quae ab illo inventore veritatis etuasi architecto beatae vitae dicta sunt explicabo.</p>
    <div class="stat" style="left:83px">
      <div class="stat-num">$25k</div>
      <div class="stat-label">AWARDED</div>
      <p class="stat-copy">Sed ut perspiciatis unde omnis iste natus<br>error sit voluptatem accusantium oremque<br>laudantium, totam rem aperiam</p>
    </div>
    <div class="stat" style="left:432px">
      <div class="stat-num">400</div>
      <div class="stat-label">STUDENTS</div>
      <p class="stat-copy">Sed ut perspiciatis unde omnis iste natus<br>error sit voluptatem accusantium oremque<br>laudantium, totam rem aperiam</p>
    </div>
    <div class="stat" style="left:782px">
      <div class="stat-num">100</div>
      <div class="stat-label">VOLUNTEERS</div>
      <p class="stat-copy">Sed ut perspiciatis unde omnis iste natus<br>error sit voluptatem accusantium oremque<br>laudantium, totam rem aperiam</p>
    </div>
  </section>

  <!-- testimonial -->
  <div class="abs quote-bg" role="img" aria-label="Soft grayscale photo of a woman sitting in an open field" style="background:radial-gradient(ellipse 120px 260px at 820px 300px,rgba(80,80,88,.45),transparent 70%),linear-gradient(180deg,#eceaed 0%,#d4d3d7 40%,#8f8e95 68%,#b7b6bb 80%,#eceaed 100%)"></div>
  <div class="abs quote-box"></div>
  <p class="abs quote-head">LOREM IPSUM DOLOR SIT AMET, CONSECTETUR ADIPISCING ELIT, SED DO<br>EIUSMOD TEMPOR INCIDIDUNT UT LABORE ET DOLORE MAGNA ALIQUA.</p>
  <p class="abs quote-copy">Sed ut perspiciatis unde omnis iste natus error sit voluptatem accusantium doloremque laudantium,<br>totam rem aperiam, eaque ipsa quae ab illo inventore veritatis et quasi architecto beatae vitae dicta<br>sunt explicabo. Nemo enim ipsam voluptatem quia voluptas</p>
  <span class="abs quote-name">MARIAROWE</span>
  <div class="abs dots"><i></i><i></i><i></i><i></i></div>

  <!-- initiatives -->
  <span class="abs ghost-num" style="left:752px;top:3405px">04</span>
  <h2 class="abs display init-title">Your Support Helps Fuel<br>Our Initiatives</h2>
  <p class="abs init-copy">Sed ut perspiciatis unde omnis iste natus error sit voluptatem accusantium doloremque laudantium, totam rem aperiam,<br>eaque ipsa quae ab illo inventore veritatis et quasi architecto beatae vitae dicta sunt explicabo.</p>

  <div class="init" style="left:101px">
    <div class="init-photo" role="img" aria-label="Group of club members cheering together outdoors among trees" style="background:radial-gradient(ellipse at 50% 70%,#9a3b3b,transparent 55%),linear-gradient(180deg,#3f6a38,#5f8a44 45%,#3b4a7a 80%,#4d6a35)"></div>
    <h3>START A CLUB</h3>
    <p>Sed ut perspiciatis unde omnis iste natus<br>error sit voluptatecusantium doloremque<br>laudantium, totam</p>
    <a class="btn">Learn More »</a>
  </div>
  <div class="init" style="left:444px">
    <div class="init-photo" role="img" aria-label="Volunteers in blue shirts packing a donations box" style="background:radial-gradient(ellipse at 55% 75%,#e2c79b,transparent 45%),linear-gradient(180deg,#b08a5c,#3b5fb0 45%,#2f4f9e 70%,#c9a978)"></div>
    <h3>FUNDRAISE</h3>
    <p>Sed ut perspiciatis unde omnis iste natus<br>error sit voluptatecusantium doloremque<br>laudantium, totam</p>
    <a class="btn">Learn More »</a>
  </div>
  <div class="init" style="left:787px">
    <div class="init-photo" role="img" aria-label="Family walking together in a park with a child on shoulders" style="background:radial-gradient(ellipse at 70% 75%,#d9a53a,transparent 40%),linear-gradient(180deg,#6d8a52,#a8b28a 40%,#3e5b8f 70%,#7a8a5a)"></div>
    <h3>PARTNER</h3>
    <p>Sed ut perspiciatis unde omnis iste natus<br>error sit voluptatecusantium doloremque<br>laudantium, totam</p>
    <a class="btn">Learn More »</a>
  </div>

  <!-- footer -->
  <footer class="abs footer">
    <div class="foot-brand">
      <span class="brand-dot"></span>
      <span class="brand-name">Tidewater Allies for Learning<br>and Mutual Aid, INC</span>
    </div>
    <div class="socials"><i></i><i></i><i></i><i></i></div>

    <div class="foot-col" style="left:477px">
      <h4>OUR COMPANY</h4>
      <ul>
        <li>Home</li><li>Services</li><li>Administration</li><li>School Readiness</li><li>Employment</li><li>About Us</li><li>Pre-apply Now</li>
      </ul>
    </div>
    <div class="foot-col" style="left:675px">
      <h4>QUICK LINKS</h4>
      <ul>
        <li>Become A Member</li><li>Resources</li><li>Take Action</li><li>Press</li><li>Get In Touch</li><li>News</li>
      </ul>
    </div>
    <div class="foot-col" style="left:881px">
      <h4>CONTACT</h4>
      <div class="contact-row">
        <span class="ic"><svg width="12" height="16" viewBox="0 0 12 16"><path d="M6 15s5-5.5 5-9A5 5 0 0 0 1 6c0 3.5 5 9 5 9z" fill="none" stroke="#fff" stroke-width="1.4"/><circle cx="6" cy="6" r="1.8" fill="#fff"/></svg></span>
        <span>4120 Harbor View Road<br>Portsmouth, Virginia 23701</span>
      </div>
      <div class="contact-row" style="align-items:center">
        <span class="ic"><svg width="13" height="13" viewBox="0 0 24 24"><path fill="#fff" d="M6.6 10.8a15 15 0 0 0 6.6 6.6l2.2-2.2c.3-.3.7-.4 1-.2 1.1.4 2.3.6 3.6.6.6 0 1 .4 1 1V20c0 .6-.4 1-1 1A17 17 0 0 1 3 4c0-.6.4-1 1-1h3.5c.6 0 1 .4 1 1 0 1.3.2 2.5.6 3.6.1.3 0 .7-.2 1z"/></svg></span>
        <span>757.555.0148</span>
      </div>
      <div class="contact-row" style="align-items:center">
        <span class="ic"><svg width="14" height="11" viewBox="0 0 24 18"><rect x="1" y="1" width="22" height="16" fill="none" stroke="#fff" stroke-width="2"/><path d="M1 1l11 9 11-9" fill="none" stroke="#fff" stroke-width="2"/></svg></span>
        <span>hello@talmaallies.org</span>
      </div>
    </div>

    <div class="foot-rule"></div>
    <p class="copyright">©Copyright 2024 TALMA, Inc. All Rights Reserved.</p>
  </footer>

</div>
</body>
</html>
```